Accounting Practice Business Card Design

I have a logo I am happy for you to use in the design of the Business Card.
You can edit and change colours as you please, I am not fixated on it.
I am looking for a modern and clean overall feel for the finished design.

The business is a small accounting practice who thrives on word of mouth referrals and this card will be given to all current and prospect clients.

Industry/Entity Type

Accountant

Contact Information for Business Card

Marcus Elwin
Level 5, 8 Corvale Ridge Road
ASHGROVE RISE VIC 3187
Phone: 9481 3057
Email: melwin@mrfaccountants.com.au
Web: www.mrfaccountants.com.au

Font styles to use
Serif
Sans Serif

Colors
0555a3
3277b5
85acd3
0393ce
33a6d7
85cae6
00a990
33b8a4
9bcb3c

Requirements
Must have
• "The end to your tax problems begin with us"
• "A referral from you is our greatest compliment"
Nice to have
• Modern clean professional

```html
<!DOCTYPE html>
<html lang="en">
<head>
<meta charset="utf-8">
<title>MRF Accountants – Business Card</title>
<link rel="stylesheet" href="https://fonts.googleapis.com/css2?family=Mulish:wght@400;700;800&display=swap">
<style>
  :root {
    --navy: #0e4378;
    --green: #3b7c34;
    --green-soft: #6fa866;
    --white: #ffffff;
    --backdrop: #e9ebee;
    --ink-soft: #dfe8f2;
  }
  * { box-sizing: border-box; margin: 0; padding: 0; }
  html, body {
    width: 1200px;
    height: 900px;
    overflow: hidden;
    background: var(--backdrop);
    font-family: "Mulish", "Century Gothic", sans-serif;
  }
  .canvas {
    width: 1200px;
    height: 900px;
    display: flex;
    flex-direction: column;
    align-items: center;
    justify-content: center;
    gap: 48px;
  }
  .card {
    width: 620px;
    height: 380px;
    position: relative;
    box-shadow: 0 10px 26px rgba(20, 40, 70, 0.18);
    overflow: hidden;
  }

  .brand-name {
    font-weight: 800;
    letter-spacing: 0.02em;
    white-space: nowrap;
    line-height: 1.1;
  }
  .tagline {
    font-weight: 400;
    font-style: italic;
    line-height: 1.35;
    text-align: center;
  }

  /* Back of card */
  .card-back {
    background: var(--navy);
    display: flex;
    flex-direction: column;
    align-items: center;
    justify-content: center;
    gap: 18px;
  }
  .card-back .inset-frame {
    position: absolute;
    inset: 22px;
    border: 1px solid var(--green);
  }
  .card-back .brand-name {
    color: var(--green);
    font-size: 56px;
  }
  .card-back .tagline {
    color: var(--ink-soft);
    font-size: 17px;
  }

  /* Front of card */
  .card-front {
    display: flex;
    background: var(--white);
  }
  .front-brand {
    flex: 0 0 47%;
    display: flex;
    flex-direction: column;
    align-items: center;
    justify-content: center;
    gap: 14px;
    padding: 0 24px;
    background: var(--white);
  }
  .front-brand .brand-name {
    color: var(--navy);
    font-size: 30px;
  }
  .front-brand .tagline {
    color: var(--green);
    font-size: 13px;
    max-width: 220px;
  }
  .front-contact {
    flex: 1;
    background: var(--navy);
    color: var(--white);
    padding: 42px 26px 0 34px;
  }
  .person-name {
    font-size: 24px;
    font-weight: 800;
    line-height: 1.15;
  }
  .person-role {
    font-size: 18px;
    font-weight: 400;
    margin-bottom: 30px;
  }
  .contact-list {
    list-style: none;
    display: flex;
    flex-direction: column;
    gap: 11px;
    font-size: 14.5px;
  }
  .contact-list li {
    display: flex;
    align-items: flex-start;
    gap: 12px;
    line-height: 1.3;
  }
  .contact-list svg {
    flex: 0 0 14px;
    width: 14px;
    height: 14px;
    margin-top: 2px;
    fill: none;
    stroke: var(--ink-soft);
    stroke-width: 1.6;
    stroke-linecap: round;
    stroke-linejoin: round;
  }
</style>
</head>
<body>
<main class="canvas">

  <section class="card card-back" aria-label="Business card back">
    <div class="inset-frame"></div>
    <span class="brand-name">MRF Accountants</span>
    <p class="tagline">The end to your tax problems begin with us</p>
  </section>

  <section class="card card-front" aria-label="Business card front">
    <div class="front-brand">
      <span class="brand-name">MRF Accountants</span>
      <p class="tagline">A referral from you is our greatest compliment</p>
    </div>
    <div class="front-contact">
      <h1 class="person-name">Marcus Elwin</h1>
      <p class="person-role">Accountant</p>
      <ul class="contact-list">
        <li>
          <svg viewBox="0 0 16 16" aria-hidden="true"><path d="M4 2l2.5 3-1.5 1.5a8 8 0 0 0 4.5 4.5L11 9.5l3 2.5-1.5 2A10 10 0 0 1 2 3.5z"/></svg>
          <span>9481 3057</span>
        </li>
        <li>
          <svg viewBox="0 0 16 16" aria-hidden="true"><rect x="4" y="2" width="8" height="4"/><rect x="2" y="6" width="12" height="6"/><rect x="4" y="10" width="8" height="4"/></svg>
          <span>9481 3099</span>
        </li>
        <li>
          <svg viewBox="0 0 16 16" aria-hidden="true"><rect x="1.5" y="3.5" width="13" height="9"/><path d="M1.5 3.5L8 9l6.5-5.5"/></svg>
          <span>melwin@mrfaccountants.com.au</span>
        </li>
        <li>
          <svg viewBox="0 0 16 16" aria-hidden="true"><circle cx="8" cy="8" r="6.5"/><path d="M1.5 8h13M8 1.5c2.2 2 2.2 11 0 13M8 1.5c-2.2 2-2.2 11 0 13"/></svg>
          <span>www.mrfaccountants.com.au</span>
        </li>
        <li>
          <svg viewBox="0 0 16 16" aria-hidden="true"><path d="M8 15s5-5 5-8.5a5 5 0 0 0-10 0C3 10 8 15 8 15z"/><circle cx="8" cy="6.5" r="1.8"/></svg>
          <span>Level 5, 8 Corvale Ridge Road<br>ASHGROVE RISE VIC 3187</span>
        </li>
      </ul>
    </div>
  </section>

</main>
</body>
</html>
```